Party planning business card design

Galas with Wren is a party planning business

Function Planning: Weddings/Themed Parties/Children's Parties

Adult and Children's Photo Booths
Party Themed boxes,
We can find the venue, entertainment. face painters.

Children's costumes and accessories - Sell / Hire

Web: www.galaswithwren.example
Facebook: Galas with Wren

Industry/Entity Type

Party Planning

Contact Information for Business Card

Galas With Wren, Rosalind Pektrew,
Creative Director

Colors
e34297
000000

Requirements
Must have
• on my logo are you able to edit the stars to pink?

```html
<!DOCTYPE html>
<html lang="en">
<head>
<meta charset="utf-8">
<title>Galas with Wren – Business Card</title>
<link rel="stylesheet" href="https://fonts.googleapis.com/css2?family=Quicksand:wght@500;700&family=Lato:wght@400;700;900&display=swap">
<style>
  :root {
    --stage: #2a2a2a;
    --pink: #e34297;
    --pink-dark: #c9327f;
    --card-white: #f7f7f7;
    --ink: #000000;
    --rule-dark: #1a1a1a;
    --tab-dark: #1c1c1c;
  }
  * { box-sizing: border-box; margin: 0; padding: 0; }
  html, body { width: 1200px; height: 900px; overflow: hidden; background: var(--stage); }
  .canvas { position: relative; width: 1200px; height: 900px; }

  /* Front card */
  .card-front {
    position: absolute; left: 70px; top: 80px; width: 540px; height: 310px;
    background: linear-gradient(160deg, var(--pink) 0%, var(--pink-dark) 100%);
    box-shadow: 0 10px 30px rgba(0,0,0,.45);
    font-family: 'Quicksand', sans-serif;
    display: flex; flex-direction: column; align-items: center; justify-content: center;
  }
  .front-name { color: #ffffff; font-size: 38px; font-weight: 700; letter-spacing: 2px; }
  .front-rule {
    width: 400px; height: 3px; margin: 18px 0 22px;
    background: linear-gradient(90deg, transparent, var(--rule-dark) 50%, transparent);
    box-shadow: 0 4px 6px rgba(0,0,0,.25);
  }
  .front-tagline { color: var(--ink); font-size: 32px; font-weight: 700; letter-spacing: 1.5px; }

  /* Back card */
  .card-back {
    position: absolute; left: 470px; top: 450px; width: 660px; height: 380px;
    background: var(--card-white);
    box-shadow: 0 10px 30px rgba(0,0,0,.45);
    font-family: 'Lato', sans-serif;
    overflow: hidden;
  }
  .brand-area {
    position: absolute; left: 40px; top: 150px; width: 330px;
    display: flex; align-items: center; gap: 14px;
  }
  .brand-dot { width: 22px; height: 22px; border-radius: 50%; background: var(--pink); flex: none; }
  .brand-name { font-size: 30px; font-weight: 700; color: var(--ink); letter-spacing: 1px; }

  .divider {
    position: absolute; left: 385px; top: 50px; width: 3px; height: 200px;
    background: linear-gradient(180deg, transparent, var(--ink) 40%, var(--ink) 60%, transparent);
  }
  .contact { position: absolute; left: 405px; top: 40px; width: 245px; }
  .contact-name { color: var(--pink); font-size: 20px; font-weight: 900; line-height: 1; white-space: nowrap; }
  .contact-role { color: var(--ink); font-size: 12px; font-weight: 700; letter-spacing: .5px; margin-top: 4px; }
  .contact-address { color: var(--pink); font-size: 14px; font-weight: 900; line-height: 1.2; margin-top: 34px; }
  .contact-line { display: flex; align-items: center; gap: 8px; font-size: 14px; color: var(--ink); margin-top: 8px; white-space: nowrap; }
  .contact-line svg { flex: none; }
  .contact-line.email { font-size: 12.5px; }
  .contact-web { color: var(--pink); font-size: 16px; font-weight: 900; margin-top: 10px; white-space: nowrap; }

  .services {
    position: absolute; right: 40px; top: 282px;
    font-size: 14px; font-weight: 700; color: var(--ink); letter-spacing: .3px;
    display: flex; align-items: center; white-space: nowrap;
  }
  .services .sep { display: inline-block; width: 3px; height: 18px; background: var(--pink); margin: 0 8px; }

  .footer-band { position: absolute; left: 0; bottom: 0; }
</style>
</head>
<body>
<main class="canvas">

  <section class="card-front" aria-label="Business card front">
    <h1 class="front-name">Galas with Wren</h1>
    <div class="front-rule"></div>
    <p class="front-tagline">We get the Party Started</p>
  </section>

  <section class="card-back" aria-label="Business card back">
    <div class="brand-area">
      <span class="brand-dot"></span>
      <span class="brand-name">Galas with Wren</span>
    </div>

    <div class="divider"></div>

    <div class="contact">
      <p class="contact-name">ROSALIND PEKTREW</p>
      <p class="contact-role">CREATIVE DIRECTOR</p>
      <p class="contact-address">#12 Larkfield Lane,<br>Marden Road, Queensland,<br>Australia 4000</p>
      <p class="contact-line">
        <svg width="16" height="14" viewBox="0 0 16 14" aria-hidden="true"><path d="M1 5 Q8 -1 15 5 L13 7 L11 5 L5 5 L3 7 Z" fill="#e34297"/><rect x="4" y="7" width="8" height="6" rx="1" fill="#e34297"/></svg>
        0400 123 987
      </p>
      <p class="contact-line email">
        <svg width="16" height="12" viewBox="0 0 16 12" aria-hidden="true"><rect x="0.5" y="0.5" width="15" height="11" fill="#e34297"/><path d="M1 1 L8 7 L15 1" stroke="#fff" stroke-width="1.4" fill="none"/></svg>
        rosalind@galaswithwren.example
      </p>
      <p class="contact-web">www.galaswithwren.example</p>
    </div>

    <p class="services">WEDDINGS<span class="sep"></span>THEMED PARTIES<span class="sep"></span>CHILDREN'S PARTIES</p>

    <svg class="footer-band" width="660" height="80" viewBox="0 0 660 80" aria-hidden="true">
      <path d="M0 80 L0 66 L470 50 L490 30 L660 24 L660 80 Z" fill="#e34297"/>
      <path d="M495 32 L660 26 L660 80 L480 80 Z" fill="#1c1c1c"/>
    </svg>
  </section>

</main>
</body>
</html>
```